Fun Language School in San Diego, CA - We want cool Business Card

We need a new business card design for our new logo. We are a language school in beautiful San Diego, California. Our target is students from all over the world who age from 18 to 25. They come to our school to learn English. Our school has a modern look, trending and fun place. We are the only language school who use tablets in class. We are student oriented, Students Come First is our slogan. We are re-branding ourselves with a new logo. We would like to see a designs that use our new logo and it should reflect the feel of young, fun, modern, high-tech and attractive to young people.
I've seen some business card designs with transparent look, unusual shapes, we are open to any cool ideas. Thank you very much!

In order for you to know more about our school, here are the links to our Vidmarlo Channel and Friendlane.

Vidmarlo: https://www.vidmarlo.example/channel/ZXpolrT-48kwb2nH7c5DqLm
Friendlane: https://www.friendlane.example/BVSchool

Target Market(s)

Our target is students from all over the world who age from 18 to 25. International students.

Industry/Entity Type

School

Font styles to use
Sans Serif

Requirements
Must have
• Our new logo. Name, title and address.
Should not have
• Other colors other than the ones we have in our logo. Characters are fine.

```html
<!DOCTYPE html>
<html lang="en">
<head>
<meta charset="utf-8">
<title>BV School – Business Card</title>
<link rel="stylesheet" href="https://fonts.googleapis.com/css2?family=Open+Sans:wght@300;400;600&display=swap">
<style>
  :root {
    --page: #e9e6e1;
    --bezel: #0c0c0e;
    --bezel-edge: #2a2a2e;
    --screen: #0b1a45;
    --gloss: rgba(150, 170, 215, 0.38);
    --text: #f2f4fa;
    --tile-white: #ffffff;
    --tile-blue: #3f5a9a;
    --tile-red: #c8242a;
    --logo-teal: #3fa7b4;
    --logo-ink: #5b6870;
  }
  * { box-sizing: border-box; margin: 0; padding: 0; }
  html, body { width: 1200px; height: 913px; overflow: hidden; }
  body {
    background: var(--page);
    font-family: "Open Sans", sans-serif;
    font-weight: 300;
    color: var(--text);
    position: relative;
  }
  .card {
    position: absolute;
    left: 150px; top: 196px;
    width: 900px; height: 520px;
    background: var(--bezel);
    border-radius: 30px;
    box-shadow: 0 0 0 2px var(--bezel-edge), 0 18px 40px rgba(0,0,0,.25);
    overflow: hidden;
  }
  .camera {
    position: absolute; left: 440px; top: 18px;
    width: 20px; height: 6px;
  }
  .camera span {
    position: absolute; top: 0; width: 6px; height: 6px; border-radius: 50%;
    background: #3a3d48;
  }
  .camera span:first-child { left: 0; }
  .camera span:last-child { left: 12px; width: 4px; height: 4px; top: 1px; }
  .screen {
    position: absolute;
    left: 50px; top: 42px; right: 50px; bottom: 42px;
    background: var(--screen);
  }
  .gloss { position: absolute; inset: 0; pointer-events: none; }
  .holder { position: absolute; top: 36px; right: 70px; text-align: left; }
  .holder-name { font-size: 36px; line-height: 1; }
  .holder-title { font-size: 18px; margin-top: 2px; padding-left: 4px; }
  .start { position: absolute; left: 70px; top: 150px; font-size: 62px; line-height: 1; }
  .section { position: absolute; left: 110px; top: 238px; font-size: 26px; }
  .school-tile {
    position: absolute; left: 130px; top: 284px;
    width: 290px; height: 118px;
    background: var(--tile-white);
    display: flex; align-items: center; justify-content: center; gap: 16px;
  }
  .school-dot { width: 54px; height: 54px; border-radius: 50%; background: var(--logo-teal); }
  .school-name { color: var(--logo-ink); font-size: 36px; font-weight: 400; }
  .links { position: absolute; left: 340px; top: 176px; }
  .link { display: flex; align-items: center; gap: 14px; height: 48px; margin-bottom: 8px; }
  .link-tile {
    width: 64px; height: 48px;
    display: flex; align-items: center; justify-content: center;
    font-size: 11px; font-weight: 400; color: var(--text);
  }
  .link-tile.social { background: var(--tile-blue); }
  .link-tile.video { background: var(--tile-red); width: 48px; margin-left: 8px; }
  .link-text { font-size: 22px; }
</style>
</head>
<body>
  <div class="card">
    <div class="camera"><span></span><span></span></div>
    <div class="screen">
      <div class="holder">
        <div class="holder-name">John Doe</div>
        <div class="holder-title">company owner</div>
      </div>
      <div class="start">Start</div>
      <div class="section">Main Apps</div>
      <div class="school-tile">
        <div class="school-dot"></div>
        <div class="school-name">BV School</div>
      </div>
      <div class="links">
        <div class="link">
          <div class="link-tile social">Friendlane</div>
          <div class="link-text">/BVSchool</div>
        </div>
        <div class="link">
          <div class="link-tile video">Vidmarlo</div>
          <div class="link-text">/user/BVS2013SanDiego</div>
        </div>
      </div>
    </div>
    <svg class="gloss" width="900" height="520" viewBox="0 0 900 520" aria-hidden="true">
      <polygon points="0,0 560,0 190,520 0,520" fill="var(--gloss)"/>
    </svg>
  </div>
</body>
</html>
```